I am a highly experienced private practice psychotherapist serving high end clientele in the Wall Street area of New York City. I need electronic letterhead (that can also be printed) to use for bills, receipts, and correspondences.

My clients are very high end and are used to elegance and wealth. The letterhead should contain the following information: Marian T. Holcombe, LCSW 72 Pellham Street, Suite 2561 New York, NY 10087 Phone : (917) 555-3194 email: therapy@marianholcombelcsw.example website: www.marianholcombelcsw.example

Thank you for your designs. Please be advised that the letterhead will be used for bills/invoices; professional letters to other mental health professionals and doctors, as well as to attorneys. It needs to be highly professional in the same way that a law firm has professional and elegant letterhead, raher than whimsical or with spa designers. My letters end up as official documents.

```html
<!DOCTYPE html>
<html lang="en">
<head>
<meta charset="UTF-8">
<title>Marian T. Holcombe, LCSW — Letterhead</title>
<link rel="stylesheet" href="https://fonts.googleapis.com/css2?family=Caladea&family=Carlito:wght@400;700&display=swap">
<style>
  :root {
    --paper: #ffffff;
    --ink: #111111;
    --rule: #1a1a1a;
  }
  * { margin: 0; padding: 0; box-sizing: border-box; }
  html, body {
    width: 800px;
    height: 1200px;
    overflow: hidden;
    background: var(--paper);
  }
  .letterhead {
    position: relative;
    width: 800px;
    height: 1200px;
    background: var(--paper);
    color: var(--ink);
  }
  .masthead-rule {
    position: absolute;
    left: 236px;
    top: 61px;
    width: 311px;
    height: 1.5px;
    background: var(--rule);
  }
  .practitioner-name {
    position: absolute;
    left: 236px;
    width: 311px;
    top: 66px;
    text-align: center;
    font-family: "Caladea", Georgia, serif;
    font-size: 40px;
    font-weight: 400;
    line-height: 1;
    letter-spacing: 0.2px;
    white-space: nowrap;
  }
  .credential {
    position: absolute;
    left: 236px;
    top: 110px;
    width: 311px;
    display: flex;
    align-items: center;
    gap: 8px;
    font-family: "Caladea", Georgia, serif;
    font-size: 21px;
    line-height: 1;
    letter-spacing: 0.5px;
  }
  .credential::before,
  .credential::after {
    content: "";
    flex: 1;
    height: 1.5px;
    background: var(--rule);
  }
  .contact {
    position: absolute;
    top: 145px;
    font-family: "Carlito", Calibri, Arial, sans-serif;
    font-size: 11.5px;
    line-height: 14.5px;
  }
  .contact-address { left: 213px; top: 147px; }
  .contact-channels { left: 385px; }
  .contact-label { font-weight: 700; }
</style>
</head>
<body>
  <main class="letterhead">
    <header>
      <div class="masthead-rule"></div>
      <h1 class="practitioner-name">Marian T. Holcombe</h1>
      <div class="credential">LCSW</div>
      <address class="contact contact-address" style="font-style:normal">
        72 Pellham Street, Suite 2561<br>
        New York, NY 10087
      </address>
      <div class="contact contact-channels">
        <div><span class="contact-label">t:</span> (917) 555-3194</div>
        <div><span class="contact-label">e:</span> therapy@marianholcombelcsw.example</div>
        <div><span class="contact-label">w:</span> www.marianholcombelcsw.example</div>
      </div>
    </header>
  </main>
</body>
</html>
```